New Website for novelty yarn producer

We need a new website for our company, Merovac. We make highly tailored yarns for weavers worldwide. This year marks our 40th anniversary and we want to evolve our image and identity.

Our temporary website can be found at:
www.merovacyarns-example.com

Our only concern in that throughout the website the protagonist must be our client, we make their creations possible and are highly adaptable both during the ideation process of the yarn as well as in the production. This is at the core of the way we do business and is summarised within the concept of OBM (Open Bridge Method).

Industry/Entity Type

Textile

Number of Pages Required

1 page

Colors
9bcb3c

Requirements
Must have
• Open Bridge Method (OBM) - can be found on or current website www.merovacyarns-example.com

```html
<!DOCTYPE html>
<html lang="en">
<head>
<meta charset="utf-8">
<title>Merovac – Tailored Weaving Solutions</title>
<link rel="stylesheet" href="https://fonts.googleapis.com/css2?family=Playfair+Display:wght@700;900&family=PT+Sans:wght@400;700&display=swap">
<style>
:root{
  --green:#9bcb3c;
  --green-dark:#7fae25;
  --ink:#1d1d1d;
  --text:#555;
  --muted:#888;
  --line:#e4e4e4;
  --footer:#1e1e1e;
  --white:#fff;
}
*{box-sizing:border-box;margin:0;padding:0}
html,body{width:1200px;height:2675px;overflow:hidden;background:var(--white)}
body{position:relative;font-family:"PT Sans",Arial,sans-serif;color:var(--text)}
.abs{position:absolute}
.serif{font-family:"Playfair Display",Georgia,serif;font-weight:900;text-transform:uppercase}

/* top bar */
.topbar{top:0;left:0;width:1200px;height:70px;background:var(--white)}
.contact-line{left:230px;font-size:10px;color:var(--ink);display:flex;align-items:center;gap:8px}
.contact-line b{font-weight:700}
.contact-line svg{width:12px;height:12px;fill:var(--green)}
.brand{left:0;width:1200px;top:12px;text-align:center;font-family:"PT Sans",Arial,sans-serif;font-weight:700;font-size:34px;letter-spacing:1px;color:var(--ink);line-height:40px}
.social-label{left:888px;top:18px;font-size:10px;font-weight:700;color:var(--ink)}
.social-dots{left:888px;top:32px;display:flex;gap:8px}
.social-dots span{width:22px;height:22px;border:1.5px solid var(--green);border-radius:50%}

/* hero */
.hero{top:70px;left:0;width:1200px;height:575px;background:radial-gradient(ellipse at 55% 45%,#6f7d79 0%,#4a5250 40%,#2c2f2f 100%)}
.nav{top:52px;left:0;width:1200px;display:flex;justify-content:center;font-size:10px;font-weight:700;color:var(--white)}
.nav a{color:var(--white);text-decoration:none;padding:0 31px;border-right:1px solid rgba(255,255,255,.6);line-height:12px}
.nav a:last-child{border-right:0}
.nav-rule{top:94px;left:0;width:1200px;height:1px;background:rgba(255,255,255,.35)}
.hero-title{top:196px;left:0;width:1200px;text-align:center;font-size:64px;line-height:70px}
.hero-title span{display:block;color:var(--white);transform:scaleX(.62);transform-origin:center}
.hero-title span.green{color:var(--green)}
.btn-white{top:400px;left:545px;width:110px;height:40px;background:var(--white);color:var(--ink);font-size:10px;font-weight:700;text-align:center;line-height:40px}
.dots{top:497px;left:586px;display:flex;gap:5px}
.dots i{width:5px;height:5px;background:#ddd}
.arrow{top:300px;width:36px;height:60px}

/* features */
.feature{top:682px;width:235px;height:200px;text-align:center}
.feature.card{box-shadow:0 0 12px rgba(0,0,0,.12);background:var(--white)}
.feature svg{margin-top:28px;width:58px;height:64px}
.feature h3{font-size:12px;color:var(--ink);margin-top:14px;letter-spacing:.3px}
.feature p{font-size:9.5px;line-height:16px;margin:6px 14px 0;color:var(--text)}
.section-shadow{top:916px;left:0;width:1200px;height:8px;background:linear-gradient(#eee,rgba(255,255,255,0))}

/* method */
.photo{position:absolute}
.method-title{top:980px;left:600px;font-size:24px;line-height:32px;color:var(--ink);transform:scaleX(.7);transform-origin:left center}
.eyebrow{font-size:9px;font-weight:700;color:var(--green)}
.rule-diamond{display:flex;align-items:center;gap:6px}
.rule-diamond i{display:block;height:1px;background:var(--green);width:100px}
.rule-diamond b{width:6px;height:6px;background:var(--green);transform:rotate(45deg)}
.method-text{top:1090px;left:600px;width:355px;font-size:10px;line-height:19px}
.btn-green{width:100px;height:34px;background:var(--green);color:var(--white);font-size:10px;font-weight:700;text-align:center;line-height:34px}

/* numbers */
.numbers{top:1352px;left:0;width:1200px;height:353px;background:linear-gradient(100deg,#2a2224 0%,#4a1e2a 35%,#3a3132 65%,#2b2627 100%)}
.numbers-title{top:52px;left:0;width:1200px;text-align:center;font-size:22px;color:var(--white)}
.numbers-title span{display:inline-block;transform:scaleX(.65)}
.stat{top:125px;width:200px;text-align:center;color:var(--white)}
.stat .hex{position:relative;width:78px;height:86px;margin:0 auto}
.stat .hex svg{position:absolute;inset:0}
.stat .hex span{position:absolute;inset:0;line-height:86px;font-size:24px}
.stat p{font-size:11px;font-weight:700;margin-top:12px}
.btn-outline{top:318px;left:543px;width:114px;height:35px;background:var(--white);color:var(--ink);font-size:10px;font-weight:700;text-align:center;line-height:35px}

/* heritage */
.heritage-title{top:1772px;left:0;width:1200px;text-align:center;font-size:22px;color:var(--ink)}
.heritage-title span{display:inline-block;transform:scaleX(.65)}
.heritage-text{top:1822px;left:360px;width:480px;text-align:center;font-size:9.5px;line-height:20px;color:var(--ink);font-weight:700}
.divider{top:1975px;left:0;width:1200px;height:2px;background:var(--line)}

/* blog */
.blog-title{top:2068px;left:200px;width:400px;text-align:right;font-size:24px;line-height:34px;color:var(--ink)}
.blog-title span{display:block;transform:scaleX(.58);transform-origin:right center}
.blog-text{top:2182px;left:262px;width:338px;text-align:right;font-size:9.5px;line-height:15px}
.comment{top:2300px;left:480px;width:120px;text-align:right;font-size:9px;color:var(--ink);font-weight:700}

/* footer */
.footer{top:2437px;left:0;width:1200px;height:238px;background:var(--footer);color:#ddd;font-size:10px}
.footer h4{position:absolute;top:52px;font-size:11px;color:var(--white);letter-spacing:.3px}
.footer ul{list-style:none;position:absolute;line-height:19px}
.f-item{position:absolute;left:230px;display:flex;gap:16px;align-items:flex-start;line-height:15px}
.f-item svg{width:16px;height:16px;fill:#eee;flex:none}
.follow li{display:flex;align-items:center;gap:8px;line-height:23px}
.follow li i{width:14px;height:14px;border:1px solid #eee;display:block}
.copy-rule{top:201px;left:0;width:1200px;height:1px;background:#333}
.copy{top:214px;font-size:9px;color:#ccc}
</style>
</head>
<body>

<header class="abs topbar">
  <div class="abs contact-line" style="top:20px">
    <svg viewBox="0 0 24 24"><path d="M6.6 10.8a15 15 0 0 0 6.6 6.6l2.2-2.2a1 1 0 0 1 1-.25 11.4 11.4 0 0 0 3.6.6 1 1 0 0 1 1 1V20a1 1 0 0 1-1 1A17 17 0 0 1 3 4a1 1 0 0 1 1-1h3.5a1 1 0 0 1 1 1c0 1.25.2 2.450.6 3.6a1 1 0 0 1-.25 1z"/></svg>
    <span><b>PHONE</b> : &nbsp;0100 55231</span>
  </div>
  <div class="abs contact-line" style="top:36px">
    <svg viewBox="0 0 24 24"><path d="M2 5h20v14H2z M4 7v.5l8 5 8-5V7z" fill-rule="evenodd"/></svg>
    <span><b>MAIL</b> &nbsp;: commerciale@merovac.example</span>
  </div>
  <div class="abs brand">MEROVAC</div>
  <div class="abs social-label">SOCIAL LINK :</div>
  <div class="abs social-dots"><span></span><span></span><span></span></div>
</header>

<section class="abs hero" role="img" aria-label="Hands holding balls of grey and teal yarn">
  <nav class="abs nav">
    <a>HOME</a><a>ABOUT US</a><a>OPEN BRIDGE METHOD</a><a>HERITAGE</a><a>TEAM</a><a>BLOG</a><a>CONTACT</a>
  </nav>
  <div class="abs nav-rule"></div>
  <svg class="abs arrow" style="left:190px" viewBox="0 0 36 60"><polyline points="30,4 6,30 30,56" fill="none" stroke="rgba(255,255,255,.45)" stroke-width="2"/></svg>
  <svg class="abs arrow" style="left:974px" viewBox="0 0 36 60"><polyline points="6,4 30,30 6,56" fill="none" stroke="rgba(255,255,255,.45)" stroke-width="2"/></svg>
  <h1 class="abs serif hero-title"><span>Tailored Weaving</span><span class="green">Solutions</span></h1>
  <a class="abs btn-white">CONTACT US</a>
  <div class="abs dots"><i></i><i></i><i></i></div>
</section>

<section>
  <article class="abs feature card" style="left:230px">
    <svg viewBox="0 0 58 64"><polygon points="29,0 58,16 58,48 29,64 0,48 0,16" fill="var(--green)"/><circle cx="29" cy="24" r="6" fill="#fff"/><path d="M18 44c2-8 20-8 22 0z" fill="#fff"/></svg>
    <h3>EXPERIENCE</h3>
    <p>Over the years the company has gained the knowledge and skills that define the superiority of our product and the rigor of our work ethic</p>
  </article>
  <article class="abs feature" style="left:483px">
    <svg viewBox="0 0 58 64"><polygon points="29,0 58,16 58,48 29,64 0,48 0,16" fill="var(--green)"/><circle cx="29" cy="28" r="9" fill="#fff"/><rect x="25" y="37" width="8" height="7" fill="#fff"/></svg>
    <h3>CREATIVITY</h3>
    <p>Our belief is that the key to our clients' success is a combination of innovation, creativity and quality. We strive to adapt and re-imagine</p>
  </article>
  <article class="abs feature" style="left:736px">
    <svg viewBox="0 0 58 64"><polygon points="29,0 58,16 58,48 29,64 0,48 0,16" fill="var(--green)"/><path d="M14 30l8-6 7 4 7-4 8 6-10 9h-10z" fill="#fff"/></svg>
    <h3>PROFESSIONALITY</h3>
    <p>We are a family business at the core. Our company is run with the same values as the Ardenti family: respect, determination and commitment.</p>
  </article>
  <div class="abs section-shadow"></div>
</section>

<section>
  <div class="photo" style="top:975px;left:500px;width:350px;height:330px;background:radial-gradient(circle at 35% 45%,#f5d9dc 0%,#fbeff0 45%,#fff 75%)" role="img" aria-label="Soft pink and white balls of yarn"></div>
  <div class="photo" style="top:975px;left:297px;width:188px;height:210px;background:linear-gradient(135deg,#3a3a3a,#555 60%,#2d2d2d);box-shadow:0 4px 10px rgba(0,0,0,.25)" role="img" aria-label="Dark woven fabric with yellow threads"></div>
  <div class="photo" style="top:1040px;left:230px;width:188px;height:255px;background:linear-gradient(160deg,#e7d23c 0%,#e05a3a 30%,#c93a7a 50%,#5bb9d6 75%,#e8efe9 100%);box-shadow:0 4px 12px rgba(0,0,0,.3)" role="img" aria-label="Rows of brightly coloured woven yarn"></div>
  <h2 class="abs serif method-title">Open Bridge<br>Method</h2>
  <div class="abs rule-diamond" style="top:1062px;left:600px"><span class="eyebrow">PRODUCTION BUILT AROUND YOU</span><b></b><i></i></div>
  <div class="abs method-text">
    <p>We believe that the key to delivering a yarn that exceeds our client's expectation is to work together with weavers from step one, starting from the desired end product and working backwards. This allows us to develop the product that our weavers need, rather than having weavers adapt to the supplied raw materials.</p>
    <p>Our Open Bridge Method consists achieving maximum flexibility both in development and production.</p>
  </div>
  <a class="abs btn-green" style="top:1232px;left:600px">LEARN MORE</a>
</section>

<section class="abs numbers" role="img" aria-label="Red yarn stretched on a weaving loom">
  <h2 class="abs serif numbers-title"><span>MYS IN NUMBERS</span></h2>
  <svg class="abs" style="top:165px;left:380px" width="440" height="4"><line x1="0" y1="2" x2="440" y2="2" stroke="#ddd" stroke-width="1.5"/></svg>
  <div class="abs stat" style="left:284px">
    <div class="hex"><svg viewBox="0 0 78 86"><polygon points="39,1 77,22 77,64 39,85 1,64 1,22" fill="#3a2d30" stroke="#eee" stroke-width="1.5"/></svg><span>40</span></div>
    <p>YEARS IN BUSNESS</p>
  </div>
  <div class="abs stat" style="left:500px">
    <div class="hex"><svg viewBox="0 0 78 86"><polygon points="39,1 77,22 77,64 39,85 1,64 1,22" fill="#3a2d30" stroke="#eee" stroke-width="1.5"/></svg><span>2</span></div>
    <p>MILLION KILOGRAMS/ YR</p>
  </div>
  <div class="abs stat" style="left:716px">
    <div class="hex"><svg viewBox="0 0 78 86"><polygon points="39,1 77,22 77,64 39,85 1,64 1,22" fill="#3a2d30" stroke="#eee" stroke-width="1.5"/></svg><span>8</span></div>
    <p>BRANDS</p>
  </div>
  <a class="abs btn-outline">FIND OUT MORE</a>
</section>

<section>
  <div class="photo" style="top:1715px;left:380px;width:440px;height:210px;background:radial-gradient(ellipse at 50% 55%,#dbe4f3 0%,#f6e2d2 35%,#fdf6e6 55%,#fff 75%)" role="img" aria-label="Pastel balls of yarn with a crochet hook"></div>
  <h2 class="abs serif heritage-title"><span>Our Heritage</span></h2>
  <p class="abs heritage-text">Our team has decades of experience in providing yarn solutions to weavers around the world, assisting them in the creation of outstanding textiles.Our clients can expect open lines of communication, clarity and professionalism.Our focus is our client.The success of a client is our success.</p>
  <div class="abs divider"></div>
</section>

<section>
  <h2 class="abs serif blog-title"><span>Merovac NYS - 40 Years</span><span>in the Making</span></h2>
  <div class="abs rule-diamond" style="top:2150px;left:410px"><i style="width:110px"></i><b></b><span class="eyebrow">MEROVAC NYS BLOG</span></div>
  <p class="abs blog-text">MEROVAC was founded in 1977, and has since supplied fine novelty yarns for the textile industry. This family owned company has carried out all operations with great respect, integrity and dedication to quality as well as creativity. We value tradition and drive innovation in all aspects of our work. MEROVAC is approaching its 40th birthday, and we believe this calls for celebration.Celebration of 40 years</p>
  <div class="abs comment">&#9633; COMMENT(0)</div>
  <a class="abs btn-green" style="top:2325px;left:498px">LEARN MORE</a>
  <div class="photo" style="top:2025px;left:655px;width:128px;height:180px;background:linear-gradient(90deg,#8a3b48,#5e6a84 40%,#a04a58 70%,#6a5d7a)" role="img" aria-label="Striped woven fabric samples"></div>
  <div class="photo" style="top:2062px;left:797px;width:128px;height:143px;background:linear-gradient(150deg,#3f4a4a,#c9c3b4 50%,#2c3434)" role="img" aria-label="Close-up of textured grey yarn"></div>
  <div class="photo" style="top:2217px;left:655px;width:128px;height:143px;background:linear-gradient(160deg,#d8d0c4,#c94a58 45%,#6a6a88 75%,#d8cfc4)" role="img" aria-label="Fanned fabric swatches in red and grey"></div>
  <div class="photo" style="top:2217px;left:797px;width:128px;height:178px;background:linear-gradient(140deg,#b04a60,#d87a8a 40%,#8a4a70 75%,#c86a7c)" role="img" aria-label="Pink and purple textured fabric"></div>
</section>

<footer class="abs footer">
  <h4 style="left:230px">KEEP IN TOUCH</h4>
  <div class="f-item" style="top:88px"><svg viewBox="0 0 24 24"><path d="M6.6 10.8a15 15 0 0 0 6.6 6.6l2.2-2.2a1 1 0 0 1 1-.25 11.4 11.4 0 0 0 3.6.6 1 1 0 0 1 1 1V20a1 1 0 0 1-1 1A17 17 0 0 1 3 4a1 1 0 0 1 1-1h3.5a1 1 0 0 1 1 1c0 1.25.2 2.45.6 3.6a1 1 0 0 1-.25 1z"/></svg><span>0100 55231</span></div>
  <div class="f-item" style="top:114px"><svg viewBox="0 0 24 24"><path d="M12 2a7 7 0 0 0-7 7c0 5 7 13 7 13s7-8 7-13a7 7 0 0 0-7-7zm0 9.5A2.5 2.5 0 1 1 12 6.5a2.5 2.5 0 0 1 0 5z"/></svg><span>Via dei Telai 12 - 00100 Borgo - Italy -<br>Tel. 0100 55231 r.a. - Fax 0100 552340</span></div>
  <div class="f-item" style="top:156px"><svg viewBox="0 0 24 24"><path d="M2 5h20v14H2z M4 7v.5l8 5 8-5V7z" fill-rule="evenodd"/></svg><span>commerciale@merovac.example</span></div>

  <h4 style="left:528px">USEFUL LINKS</h4>
  <ul style="top:84px;left:528px"><li>Home</li><li>About Us</li><li>Open Bridge Method</li><li>Heritage</li></ul>
  <ul style="top:84px;left:735px"><li>Team</li><li>Blog</li><li>Contact</li><li>Privacy Policy</li></ul>

  <h4 style="left:891px">FOLLOW US</h4>
  <ul class="follow" style="top:80px;left:897px"><li><i></i>Loomboard</li><li><i></i>Chirpline</li><li><i></i>Pinweave</li><li><i></i>Searchway</li></ul>

  <div class="abs copy-rule"></div>
  <p class="abs copy" style="left:230px">© Copyright 2018 merovacyarns. All Rights Reserved.</p>
  <p class="abs copy" style="left:812px">Privacy Policy &nbsp;| &nbsp;Terms and Conditions</p>
</footer>

</body>
</html>
```